Business Card Design

​Silver Harbor Grooves provides personal, friendly service in a fun and high energy environment. We are based in Vermont.

We would like a card that appeals to a wide range of audiences as we do a wide range of events. Please feel free to check out our website silverharborgrooves.com for inspiration.

Target Market(s)

weddings, corporate, birthday parties, colleges

Industry/Entity Type

Business

Contact Information for Business Card

Silver Harbor Grooves
Providing Entertainment For All Occasions
555 218 6093
silverharborgrooves@mailvane.com
silverharborgrooves.com

```html
<!DOCTYPE html>
<html lang="en">
<head>
<meta charset="utf-8">
<title>Silver Harbor Grooves — Business Card</title>
<link href="https://fonts.googleapis.com/css2?family=Questrial&family=Cormorant+SC:wght@600&display=swap" rel="stylesheet">
<style>
  :root {
    --stage: #1e1e1e;
    --card: #ffffff;
    --green: #2f6a26;
    --green-soft: rgba(47, 106, 38, 0.35);
    --red: #c0303a;
    --red-soft: rgba(192, 48, 58, 0.35);
    --ink: #2a2a2a;
  }
  * { margin: 0; padding: 0; box-sizing: border-box; }
  html, body { width: 1200px; height: 871px; overflow: hidden; background: var(--stage); }
  .stage {
    width: 1200px; height: 871px;
    display: flex; flex-direction: column; align-items: center; justify-content: center;
    gap: 24px;
  }
  .card {
    position: relative;
    width: 700px; height: 400px;
    background: var(--card);
    overflow: hidden;
    font-family: "Questrial", sans-serif;
    color: var(--ink);
  }
  .card--back { display: flex; align-items: center; justify-content: center; }
  .brand-name {
    font-family: "Questrial", sans-serif;
    color: var(--green);
    letter-spacing: 0.02em;
    text-transform: uppercase;
  }
  .card--back .brand-name { font-size: 44px; }
  .card--front .brand-name {
    position: absolute; left: 86px; top: 64px;
    font-size: 24px;
  }
  .holder {
    position: absolute; left: 86px; top: 148px;
  }
  .holder__name {
    font-family: "Cormorant SC", serif;
    font-weight: 600;
    font-size: 19px;
    color: var(--green);
    letter-spacing: 0.04em;
  }
  .holder__role {
    margin-top: 4px;
    font-size: 12px;
    color: var(--red);
  }
  .contacts {
    position: absolute; left: 66px; top: 240px;
    list-style: none;
    display: flex; flex-direction: column; gap: 12px;
  }
  .contacts__item {
    display: flex; align-items: center; gap: 14px;
    font-size: 14px; color: var(--ink);
  }
  .contacts__icon { width: 16px; height: 16px; flex: none; }
  .decor-area {
    position: absolute; right: 0; bottom: 0;
    width: 380px; height: 280px;
    background:
      linear-gradient(180deg, var(--red-soft) 0%, rgba(255,255,255,0) 55%),
      linear-gradient(20deg, var(--green-soft) 0%, rgba(255,255,255,0) 60%);
    -webkit-mask-image: linear-gradient(90deg, transparent 0%, #000 45%);
            mask-image: linear-gradient(90deg, transparent 0%, #000 45%);
  }
</style>
</head>
<body>
<main class="stage">
  <section class="card card--back" aria-label="Card back">
    <h1 class="brand-name">Silver Harbor Grooves</h1>
  </section>

  <section class="card card--front" aria-label="Card front">
    <div class="decor-area" role="img" aria-label="Faint decorative brand artwork in green and red tones"></div>
    <h2 class="brand-name">Silver Harbor Grooves</h2>
    <div class="holder">
      <p class="holder__name">Dara Quill</p>
      <p class="holder__role">CEO</p>
    </div>
    <ul class="contacts">
      <li class="contacts__item">
        <svg class="contacts__icon" viewBox="0 0 16 16" aria-hidden="true">
          <path d="M2 5c0-2 3-3 6-3s6 1 6 3v1h-3V4.5H5V6H2z" fill="var(--green)"/>
          <rect x="3" y="7" width="10" height="7" rx="1.5" fill="none" stroke="var(--green)" stroke-width="1.5"/>
          <circle cx="8" cy="10.5" r="1.5" fill="var(--green)"/>
        </svg>
        555 218 6093
      </li>
      <li class="contacts__item">
        <svg class="contacts__icon" viewBox="0 0 16 16" aria-hidden="true">
          <rect x="1.5" y="3.5" width="13" height="9" fill="none" stroke="var(--green)" stroke-width="1.5"/>
          <path d="M1.5 3.5 8 9l6.5-5.5" fill="none" stroke="var(--green)" stroke-width="1.5"/>
        </svg>
        silverharborgrooves@mailvane.com
      </li>
      <li class="contacts__item">
        <svg class="contacts__icon" viewBox="0 0 16 16" aria-hidden="true">
          <circle cx="8" cy="8" r="6.5" fill="none" stroke="var(--green)" stroke-width="1.5"/>
          <ellipse cx="8" cy="8" rx="2.8" ry="6.5" fill="none" stroke="var(--green)" stroke-width="1.2"/>
          <path d="M1.5 8h13" stroke="var(--green)" stroke-width="1.2"/>
        </svg>
        silverharborgrooves.com
      </li>
    </ul>
  </section>
</main>
</body>
</html>
```